Hvac and insulation company needs good looking business card design

We are hvac and insulation company and looking for a new business cards that look to today standards designs

Target Market(s)

homeowners

Industry/Entity Type

Hvac

Contact Information for Business Card

Name: Dorian Velkova
Home comfort consultant
address: 4827 Marrow Ridge Rd #215 Oakland, CA 94611
office: 888-317-5069
cell: 510-642-1388
Lic.# 458127
Email: dorian@quarry-hvac.com
Web: quarry-hvac.com

Requirements
Must have
• clean and sleek look
Nice to have
• simple with a clean look
Should not have
• to busy business card

```html
<!DOCTYPE html>
<html lang="en">
<head>
<meta charset="utf-8">
<title>Quarry Home Solutions – Business Card</title>
<link rel="stylesheet" href="https://fonts.googleapis.com/css2?family=Bebas+Neue&family=Work+Sans:wght@400;500&display=swap">
<style>
  :root {
    --backdrop: #262626;
    --card: #161616;
    --card-sheen: #222222;
    --accent: #f7861e;
    --ink: #f2f2f2;
    --font-text: "Work Sans", Arial, sans-serif;
    --font-name: "Bebas Neue", "Oswald", sans-serif;
  }
  * { margin: 0; padding: 0; box-sizing: border-box; }
  html, body {
    width: 1200px; height: 900px; overflow: hidden;
    background: var(--backdrop);
    font-family: var(--font-text);
    color: var(--ink);
  }
  .sheet { position: relative; width: 1200px; height: 900px; }
  .card {
    position: absolute; left: 250px; width: 700px; height: 400px;
    background: linear-gradient(135deg, var(--card) 0%, var(--card-sheen) 70%, var(--card) 100%);
    border-bottom: 6px solid var(--accent);
  }
  .card--front { top: 35px; }
  .card--back { top: 465px; }

  /* Front */
  .brand {
    position: absolute; top: 130px; left: 0; right: 0;
    display: flex; align-items: center; justify-content: center; gap: 18px;
  }
  .brand__mark { width: 44px; height: 44px; background: var(--accent); }
  .brand__name {
    font-weight: 500; font-size: 46px; color: var(--accent);
    letter-spacing: 1px; line-height: 1;
  }
  .license {
    position: absolute; bottom: 40px; left: 0; right: 0;
    text-align: center; font-size: 19px; letter-spacing: 1.5px;
  }

  /* Back */
  .person { position: absolute; left: 80px; top: 150px; }
  .person__name {
    font-family: var(--font-name); font-size: 46px; line-height: 1;
    color: var(--accent); letter-spacing: 0.5px;
  }
  .person__role { font-size: 17px; letter-spacing: 1px; margin-top: 6px; }
  .divider {
    position: absolute; left: 355px; top: 140px; width: 3px; height: 92px;
    background: var(--accent);
  }
  .contacts { position: absolute; left: 385px; top: 138px; list-style: none; }
  .contacts li {
    display: flex; align-items: center; gap: 10px;
    font-size: 17px; letter-spacing: 0.8px; line-height: 24px;
  }
  .contacts svg { width: 13px; height: 13px; flex: none; }
  .contacts .web-domain { color: var(--accent); }
  .address {
    position: absolute; left: 85px; bottom: 48px;
    display: flex; align-items: center; gap: 14px;
    font-size: 18px; letter-spacing: 1px;
  }
  .address svg { width: 20px; height: 24px; }
</style>
</head>
<body>
<div class="sheet">
  <section class="card card--front">
    <div class="brand">
      <span class="brand__mark"></span>
      <span class="brand__name">Quarry Home Solutions</span>
    </div>
    <p class="license">Lic.# 458127</p>
  </section>

  <section class="card card--back">
    <div class="person">
      <h1 class="person__name">Dorian Velkova</h1>
      <p class="person__role">Home comfort consultant</p>
    </div>
    <div class="divider"></div>
    <ul class="contacts">
      <li>
        <svg viewBox="0 0 16 16" fill="#f7861e"><path d="M3 1l3 3-1.5 2a9 9 0 005.5 5.5L12 10l3 3-2 2C7 15 1 9 1 3z"/></svg>
        888-317-5069
      </li>
      <li>
        <svg viewBox="0 0 16 16" fill="none" stroke="#f7861e" stroke-width="1.6"><rect x="4" y="1" width="8" height="14" rx="1.5"/><line x1="7" y1="12.5" x2="9" y2="12.5"/></svg>
        510-642-1388
      </li>
      <li>
        <svg viewBox="0 0 16 16" fill="none" stroke="#f7861e" stroke-width="1.6"><rect x="1" y="3" width="14" height="10"/><path d="M1 3l7 6 7-6"/></svg>
        dorian@quarry-hvac.com
      </li>
      <li>
        <svg viewBox="0 0 16 16" fill="none" stroke="#f7861e" stroke-width="1.4"><circle cx="8" cy="8" r="6.5"/><ellipse cx="8" cy="8" rx="3" ry="6.5"/><line x1="1.5" y1="8" x2="14.5" y2="8"/></svg>
        <span>www.<span class="web-domain">quarry-hvac</span>.com</span>
      </li>
    </ul>
    <p class="address">
      <svg viewBox="0 0 20 24" fill="#f7861e"><path d="M10 0a8 8 0 00-8 8c0 6 8 16 8 16s8-10 8-16a8 8 0 00-8-8zm0 11a3 3 0 110-6 3 3 0 010 6z"/></svg>
      4827 Marrow Ridge Rd #215 Oakland, CA 94611
    </p>
  </section>
</div>
</body>
</html>
```